Web Design Project

I have a website which looks dull and uninteresting. I'd like to apply a fresh and clean look to it, which better reflects the quality of the service I sell.The website address is http://www.brightquillpages.co.uk.

Target Market(s)

Financial advisers (financially sophisticated individuals)

Industry/Entity Type

It Service

Requirements
Should not have
• Please do not use obvious but irrelevant and boring imagery such as banks, pages from the MQ, money, books or libraries. Prefer slick relevant graphics and crisp typography.

```html
<!DOCTYPE html>
<html lang="en">
<head>
<meta charset="utf-8">
<title>BrightQuillPages</title>
<link href="https://fonts.googleapis.com/css2?family=Open+Sans:wght@400;600;700;800&display=swap" rel="stylesheet">
<style>
:root{
  --page:#f1f1f1;
  --panel:#ffffff;
  --ink:#333638;
  --muted:#8a8d90;
  --link:#2a6fb0;
  --bar:#3c4046;
  --bar-text:#ffffff;
  --accent:#3d8fd6;
  --rule:#dcdcdc;
  --footer:#2b2e33;
  --footer-text:#a4a8ad;
  --nav:#e4e4e4;
}
*{box-sizing:border-box;margin:0;padding:0}
html,body{width:1200px;height:2688px;overflow:hidden}
body{background:var(--page);font-family:"Open Sans",Arial,sans-serif;color:var(--ink);font-size:15px;line-height:1.55;position:relative}
a{color:var(--link)}
.site-header{height:110px;position:relative;background:var(--panel);border-bottom:1px solid var(--rule)}
.brand{position:absolute;left:88px;top:36px;display:flex;align-items:center;gap:10px;font-size:30px;font-weight:700;color:var(--ink);letter-spacing:-.5px}
.brand-mark{width:26px;height:26px;background:var(--accent)}
.signup{position:absolute;left:478px;top:42px;background:var(--accent);color:#fff;font-size:13px;font-weight:700;padding:7px 18px;border-radius:3px}
.main-nav{position:absolute;right:88px;top:38px;display:flex;background:var(--nav);border:1px solid #cfcfcf;border-radius:3px;font-size:13px}
.main-nav span{padding:8px 16px;border-left:1px solid #cfcfcf;color:#444}
.main-nav span:first-child{border-left:0;display:flex;align-items:center}
.hero{text-align:center;padding-top:34px;height:282px}
.hero h1{font-size:46px;font-weight:800;letter-spacing:-1px;color:#2f3235}
.hero p{color:var(--muted);font-size:16px;width:860px;margin:8px auto 0}
.jump-links{margin-top:28px;font-size:14px;color:var(--muted)}
.jump-links a{text-decoration:none;margin:0 10px}
.section{width:1024px;margin:0 auto 18px;background:var(--panel);border:1px solid var(--rule)}
.samples{min-height:460px}
.writers{min-height:348px}
.no-lifting{min-height:160px}
.faqs{min-height:302px}
.terms{min-height:230px}
.section-bar{height:46px;background:var(--bar);color:var(--bar-text);display:flex;align-items:center;justify-content:space-between;padding:0 22px}
.section-bar h2{font-size:15px;font-weight:700;letter-spacing:.5px}
.to-top{font-size:12px;background:#50555c;padding:3px 12px;border-radius:10px;color:#d8dadd}
.section-body{padding:20px 28px}
.section-body p{margin-bottom:14px}
.section-body p:last-child{margin-bottom:0}
.lead{font-weight:600}
.sample-list{list-style:none}
.sample-list li{line-height:1.7}
.subhead{font-weight:700}
.site-footer{position:absolute;left:0;top:2192px;width:1200px;height:496px;background:var(--footer);color:var(--footer-text);font-size:14px}
.footer-cols{display:flex;padding:46px 0 0 88px}
.footer-cols div{width:266px}
.footer-cols h3{color:#fff;font-size:15px;font-weight:700;margin-bottom:10px}
.footer-cols li{list-style:none;line-height:1.8}
.copyright{position:absolute;left:0;right:0;bottom:54px;text-align:center;font-size:12px;color:#7c8086;border-top:1px solid #3c4046;padding-top:24px;margin:0 88px}
.dots{display:flex;justify-content:center;gap:8px;margin-bottom:8px}
.dots span{width:12px;height:12px;border-radius:50%;background:#50555c}
</style>
</head>
<body>
<header class="site-header">
  <div class="brand"><span class="brand-mark"></span>BrightQuillPages</div>
  <div class="signup">SIGN UP</div>
  <nav class="main-nav">
    <span><svg width="14" height="13" viewBox="0 0 14 13"><path d="M7 1 1 6.5h2V12h3V8.5h2V12h3V6.5h2z" fill="#555"/></svg></span>
    <span>New Page ▾</span><span>A–Z Articles</span><span>Enter the library</span><span>Contact Us</span>
  </nav>
</header>

<section class="hero">
  <h1>New page slogan &lt;Catchy Phrase&gt;</h1>
  <p>New page sub-slogan or statement of value. A short supporting line with helpful information, that might span two or more lines of text.</p>
  <div class="jump-links"><a href="#">Samples</a>|<a href="#">The people who write the articles</a>|<a href="#">Please don't lift our words</a>|<a href="#">Some FAQs</a>|<a href="#">T &amp; Cs</a></div>
</section>

<section class="section samples">
  <div class="section-bar"><h2>SAMPLES</h2></div>
  <div class="section-body">
    <p class="lead">When you follow a link, a PDF will open. By the way, we've invested a lot of hours building the BrightQuillPages library, so it's annoying when somebody somewhere steals from us, because copying our words amounts to stealing. So please don't think we're being precious when we ask you very politely, not to copy and use these files! Thanks.</p>
    <ul class="sample-list">
      <li><a href="#">Asset allocation</a></li>
      <li><a href="#">Individual Savings Account</a></li>
      <li><a href="#">Critical Illness Insurance</a></li>
      <li><a href="#">Core Satellite Investing</a></li>
      <li><a href="#">Annuities – Basics</a></li>
      <li><a href="#">Self Invested Personal Pension</a></li>
      <li><a href="#">Inheritance Tax Planning – it's all about guessing and waiting!</a></li>
      <li><a href="#">Why financial advice can never be free</a></li>
      <li><a href="#">The Financial Services Compensation Scheme</a></li>
      <li><a href="#">Risk Profile Questionnaire</a></li>
      <li><a href="#">Behavioural Finance</a></li>
    </ul>
  </div>
</section>

<section class="section writers">
  <div class="section-bar"><h2>THE PEOPLE WHO WRITE THE ARTICLES</h2><span class="to-top">Go to top of page ↑</span></div>
  <div class="section-body">
    <p class="lead">Having written about the subject of money for twenty years, we have a thorough understanding of many different types of financial products, topics and subjects…</p>
    <p>We're not just talking about collective investments or personal pensions or insurances, or financial advice generally, but specific aspects such as SIPP, Dark Pool trading, core‑satellite investing and structured investments.</p>
    <p>Perhaps you want us to write about retirement matters and options? No problem – we've developed stuff for pensions in divorce, pensions for dentists and trivial pensions as well as SIPPs and SSASs. General guides to mortgages, insurance and investment? Yes, been there, done those and got all the T shirts. Ask us about IHT mitigation planning, probate services or behavioural finance and we can give you chapter and verse.</p>
    <p>For more about the people behind BrightQuillPages, <a href="#">please go here</a>.</p>
  </div>
</section>

<section class="section no-lifting">
  <div class="section-bar"><h2>PLEASE DON'T LIFT OUR WORDS</h2><span class="to-top">Go to top of page ↑</span></div>
  <div class="section-body">
    <p class="lead">Regrettably, there are always one or two people looking for something for nothing.</p>
    <p>So just to be on the safe side, we subscribe to a program which automatically informs us if any of our articles have been used without our permission or payment. The service is called <a href="#">PageGuard</a>.</p>
  </div>
</section>

<section class="section faqs">
  <div class="section-bar"><h2>FAQS</h2><span class="to-top">Go to top of page ↑</span></div>
  <div class="section-body">
    <p class="lead">If you have questions which are not answered here, please call 0207 5550 182 or <a href="#">email us</a>.</p>
    <p class="subhead" style="margin-bottom:0">Personalisation and tweaking</p>
    <p>If you would like us to personalise any of the articles so that they relate directly to the style or approach of your practice, are more specific, or contain advice, we can do that for you. Please <a href="#">contact us</a> for further details.</p>
    <p class="subhead" style="margin-bottom:0">Compliance</p>
    <p>Pre-written content is provided subject to industry standard terms and conditions. Whilst we will make every reasonable effort to ensure the content is compliant, BrightQuillPages will not be held responsible for any article's compliant status.</p>
  </div>
</section>

<section class="section terms">
  <div class="section-bar"><h2>TERMS &amp; CONDITIONS</h2><span class="to-top">Go to top of page ↑</span></div>
  <div class="section-body">
    <p>These articles can only be used by firms or individuals who are members – even though our articles are copyright free, please do not give them away, syndicate them or sell them to anyone else.</p>
    <p>If you become a member and then take the view – within 31 days – that our words are not up to the mark, we'll give you your money back.</p>
    <p><a href="#">Subscribe</a></p>
  </div>
</section>

<footer class="site-footer">
  <div class="footer-cols">
    <div><h3>Quick Links</h3><ul><li>Home</li><li>Articles</li><li>Support</li><li>Contact</li><li>Login</li></ul></div>
    <div><h3>Connect With Us</h3><ul><li>Newsletter</li><li>Updates</li></ul></div>
    <div><h3>Get in Touch</h3><ul><li>Contact form</li><li>Email us</li></ul></div>
    <div><h3>Help</h3><ul><li>Support</li><li>FAQ</li><li>Help</li></ul></div>
  </div>
  <div class="copyright">
    <div class="dots"><span></span><span></span><span></span></div>
    Copyright © 2013 BrightQuillPages · All rights reserved
  </div>
</footer>
</body>
</html>
```